Billboard for Real Estate Agent

I need a signage design for my billboard that is going up end of December.

-I target the higher end waterfront properties ($1,000,000 +) in Corella Bend, QLD, Australia so it needs to be sleek, funky yet sophisticated and professional and needs to have my photo- or if you have an idea with someone else's photo, then I can have one taken that's the same.

-The purpose is to target those who are thinking about selling/buying property.
We want people to remember the ad, so it's top of mind.

-The billboard is on the side of the road, and will be lit up at night and I'll have it for 13 months. Needs to be noticeable from the road, but nothing tacky and too loud.

Needs to have my name, Mara Pendleby and my contact number and business logo (attached).

Mara Pendleby
0462 913 517

Target Market(s)

Wealthy demographic 25-65 years old.

Industry/Entity Type

Business

Requirements
Must have
• My name, phone number and HOMVEX logo attached.

Bix Guidelines:
http://www.bixmedia.example/our-resources/artwork-guidelines/

Heading: Don't be a Dinosaur
Subline: Think Differently

Use one of the photos.
Nice to have
• -Quirky, different and captivating (i've attached some wacky billboard ideas)

```html
<!DOCTYPE html>
<html lang="en">
<head>
<meta charset="utf-8">
<title>Corella Bend Billboard – Mara Pendleby</title>
<link href="https://fonts.googleapis.com/css2?family=Pacifico&family=Open+Sans:ital,wght@0,700;0,800;1,700&family=Open+Sans+Condensed:wght@700&display=swap" rel="stylesheet">
<style>
  :root{
    --page:#f2f2f4;
    --night-top:#2e2c66;
    --night-mid:#4a4784;
    --night-low:#5e5b93;
    --water:#2a2a55;
    --gold:#f7a823;
    --ink-purple:#3a3461;
    --white:#ffffff;
    --badge:#0b0b0d;
  }
  html,body{margin:0;padding:0;overflow:hidden;}
  body{
    width:927px;height:1200px;background:var(--page);
    display:flex;align-items:center;justify-content:center;
  }
  .billboard{
    position:relative;width:927px;height:491px;overflow:hidden;
    background:linear-gradient(180deg,var(--night-top) 0%,var(--night-mid) 45%,var(--night-low) 68%,var(--water) 100%);
  }
  .skyline-photo{
    position:absolute;left:232px;top:170px;width:695px;height:230px;
    background:linear-gradient(180deg,rgba(94,91,147,0) 0%,#7c6f8e 35%,#c9955a 62%,#a7733f 78%,#3b3763 100%);
    opacity:.85;
  }
  .water{
    position:absolute;left:0;top:400px;width:927px;height:91px;
    background:linear-gradient(180deg,#3b3a6c,var(--water));
  }
  .agent-photo{
    position:absolute;left:0;top:42px;width:242px;height:449px;
    background:linear-gradient(180deg,#8a5a3e 0%,#6b4630 30%,#1c1a22 55%,#121116 100%);
    border-radius:110px 110px 0 0;
  }
  .kicker{
    position:absolute;left:313px;top:62px;margin:0;
    font:italic 700 26px/1 "Open Sans",sans-serif;color:var(--ink-purple);
    letter-spacing:-.5px;
  }
  .suburb{
    position:absolute;left:248px;top:74px;margin:0;
    font:400 76px/1.2 "Pacifico",cursive;color:var(--gold);
    letter-spacing:-1px;
  }
  .agent-name{
    position:absolute;left:372px;top:168px;margin:0;
    font:400 58px/1.2 "Pacifico",cursive;color:var(--white);
  }
  .contact{
    position:absolute;left:379px;top:413px;margin:0;
    font:700 34px/1 "Open Sans Condensed","Open Sans",sans-serif;color:var(--gold);
  }
  .contact .phone{color:var(--white);font-family:"Open Sans",sans-serif;font-weight:800;font-size:31px;margin-left:8px;}
  .brand-badge{
    position:absolute;left:810px;top:327px;width:68px;height:107px;
    background:var(--badge);display:flex;align-items:center;justify-content:center;
  }
  .brand-badge span{
    font:700 13px/1 "Open Sans",sans-serif;color:var(--white);letter-spacing:.5px;
  }
</style>
</head>
<body>
  <section class="billboard">
    <div class="skyline-photo" role="img" aria-label="Photo of the coastal city skyline at dusk, golden-lit towers along the beach"></div>
    <div class="water"></div>
    <div class="agent-photo" role="img" aria-label="Portrait photo of agent Mara Pendleby in a black blouse"></div>
    <p class="kicker">Now Showing</p>
    <h1 class="suburb">Corella Bend</h1>
    <h2 class="agent-name">Mara Pendleby</h2>
    <p class="contact">Call for info:<span class="phone">0462 913 517</span></p>
    <div class="brand-badge"><span>HOMVEX</span></div>
  </section>
</body>
</html>
```